Cash Pay Massage Therapy Services for Medical & Therapy Clinics

We are rolling out a new Massage Therapy service in our medical clinics, staffed by licensed professionals. Our offices have a feel between medical clinic and spa. We would like to have some small 8.5x11 posters that let the patients know that we also provide Massages at $80/60 minutes and $50/30 minutes. Typically we always bill insurance but this service would accept cash or credit card.

Target Market(s)

patients that are already having services in our medical offices. Typically, they are already being seen for massage therapy that is billing to their insurance. But, they love their therapist and want to continue to see them when insurance doesnt pay anymore.

Industry/Entity Type

Massage Therapy

Requirements
Must have
• professional (more rehabilitative/less spa) appearance. Prices, logo
Nice to have
• a similar aesthetic to our website.

```html
<!DOCTYPE html>
<html lang="en">
<head>
<meta charset="utf-8">
<title>Stillpoint – Massages</title>
<link rel="stylesheet" href="https://fonts.googleapis.com/css2?family=Jost:wght@300;400;600;700&display=swap">
<style>
  :root {
    --paper: #f7f4f1;
    --skin-light: #e6d6cb;
    --skin-mid: #c9ae9d;
    --skin-deep: #9d8170;
    --ink: #1c1b1a;
    --white: #ffffff;
    --tag-bg: #2d2a28;
  }
  * { margin: 0; padding: 0; box-sizing: border-box; }
  html, body {
    width: 972px;
    height: 1200px;
    overflow: hidden;
    background: var(--paper);
  }
  .poster {
    position: relative;
    width: 972px;
    height: 1200px;
    overflow: hidden;
    font-family: "Jost", "Century Gothic", sans-serif;
  }
  .hero-photo {
    position: absolute;
    inset: 0;
    background:
      radial-gradient(ellipse 360px 260px at 640px 620px, rgba(180,150,132,0.55), transparent 70%),
      radial-gradient(ellipse 420px 420px at 260px 700px, var(--skin-mid), transparent 72%),
      radial-gradient(ellipse 380px 260px at 260px 430px, var(--skin-deep), transparent 70%),
      linear-gradient(180deg, #f3ede8 0%, var(--skin-light) 30%, #d8c3b5 60%, #efe7e1 88%, #faf8f6 100%);
  }
  .brand {
    position: absolute;
    top: 50px;
    right: 63px;
    width: 314px;
    height: 144px;
    background: var(--ink);
    display: flex;
    align-items: flex-end;
    justify-content: center;
    padding-bottom: 22px;
  }
  .brand-name {
    color: var(--white);
    font-weight: 400;
    font-size: 58px;
    letter-spacing: -1px;
    line-height: 1;
  }
  .tagline {
    position: absolute;
    top: 214px;
    right: 63px;
    text-align: right;
    color: var(--ink);
    font-weight: 400;
    font-size: 50px;
    line-height: 1.22;
  }
  .offer {
    position: absolute;
    top: 665px;
    right: 63px;
    text-align: right;
    color: var(--white);
  }
  .offer-title {
    font-weight: 700;
    font-size: 60px;
    line-height: 1.1;
  }
  .offer-price {
    font-weight: 300;
    font-size: 66px;
    line-height: 1.25;
  }
  .offer-note {
    margin-top: 12px;
    font-weight: 600;
    font-size: 21px;
    line-height: 1.4;
  }
  .web-tag {
    position: absolute;
    top: 1095px;
    right: 63px;
    width: 337px;
    height: 54px;
    background: var(--tag-bg);
    color: var(--white);
    font-weight: 400;
    font-size: 29px;
    display: flex;
    align-items: center;
    justify-content: center;
  }
</style>
</head>
<body>
  <main class="poster">
    <div class="hero-photo" role="img" aria-label="Photograph of a woman relaxing face down on a massage table while a therapist's hand rests on her shoulder"></div>

    <div class="brand">
      <span class="brand-name">stillpoint</span>
    </div>

    <p class="tagline">Rest easy.<br>Heal steady.</p>

    <section class="offer">
      <h1 class="offer-title">MASSAGES</h1>
      <p class="offer-price">$80/60 MINUTES</p>
      <p class="offer-price">$50/30 MINUTES</p>
      <p class="offer-note">Typically we always bill insurance<br>but this service would accept<br>cash or credit card.</p>
    </section>

    <div class="web-tag">stillpointcare.com</div>
  </main>
</body>
</html>
```